New Template design for Website in Wordpress

We are interested in changing our website look at www.cargolinx.com -We also are very interested in Have it done in Wordpress in which we are understanding the search engines are liking a bit more. The website we would want to try working with on this is www.cargolinx.com. We look forward to seeing the different design ideas please just make sure they are in wordpress! Thanks, Marlen

Reason: need more design idea..... We would still like to use our pictures off our site since we paid for them so keep that in mind as well as we would still want the rotating pictures in the head of the page but not in Flash.

```html
<!DOCTYPE html>
<html lang="en">
<head>
<meta charset="utf-8">
<title>Cargolinx — A Diversified Freight Company</title>
<link href="https://fonts.googleapis.com/css2?family=Open+Sans:wght@300;400;600;700&family=Ubuntu:wght@500;700&family=Arvo:wght@700&display=swap" rel="stylesheet">
<style>
  :root {
    --brand-red: #8e1414;
    --button-red: #a3171a;
    --button-red-dark: #7d1012;
    --navy: #1c2740;
    --navy-deep: #1a233a;
    --ink: #333a44;
    --muted: #666;
    --sand: #f3e9cd;
    --sand-line: #e4d8b6;
    --card: #f7f7f7;
    --card-edge: #dedede;
  }
  * { box-sizing: border-box; margin: 0; padding: 0; }
  html, body { width: 952px; height: 1200px; overflow: hidden; }
  body { position: relative; background: #fff; font-family: "Open Sans", Arial, sans-serif; color: var(--ink); }

  /* Header */
  .site-header {
    position: absolute; left: 0; top: 0; width: 952px; height: 90px;
    background: linear-gradient(#ffffff, #f3f3f3);
    border-bottom: 1px solid #dcdcdc;
  }
  .brand { position: absolute; left: 99px; top: 34px; }
  .brand-name { font-family: "Open Sans", Arial, sans-serif; font-weight: 700; font-size: 18px; color: var(--brand-red); letter-spacing: -0.3px; line-height: 1; }
  .brand-tagline { font-size: 8.5px; color: var(--muted); margin-top: 3px; text-transform: uppercase; letter-spacing: 0.1px; }
  .contact-phone { position: absolute; left: 718px; top: 14px; display: flex; align-items: center; gap: 9px; }
  .contact-phone span { font-size: 15px; font-weight: 600; color: var(--brand-red); }
  .main-nav { position: absolute; top: 57px; left: 490px; display: flex; align-items: center; }
  .main-nav a { font-size: 11.5px; color: #111; text-decoration: none; text-transform: uppercase; height: 22px; line-height: 22px; }
  .main-nav .is-current { background: var(--brand-red); color: #fff; padding: 0 7px; border-radius: 2px; margin-right: 16px; }
  .main-nav .nav-gap { margin-right: 26px; }

  /* Hero slider */
  .hero { position: absolute; left: 100px; top: 101px; width: 752px; height: 300px; border-radius: 4px; overflow: hidden; }
  .hero-shadow { position: absolute; left: 110px; top: 398px; width: 732px; height: 32px; background: radial-gradient(ellipse at top, rgba(0,0,0,.22), rgba(0,0,0,0) 70%); }
  .hero-photo { position: absolute; inset: 0; background: linear-gradient(180deg, #a9c6dc 0%, #c9b48a 30%, #9a6e4a 52%, #2b2a2e 68%, #2a4f73 82%, #3f6f96 100%); }
  .hero-caption { position: absolute; left: 12px; top: 102px; width: 232px; height: 150px; background: rgba(40,40,40,.85); }
  .hero-title { position: absolute; left: 18px; top: 28px; font-family: "Ubuntu", Arial, sans-serif; font-weight: 700; font-size: 22.5px; line-height: 28px; color: #fff; text-transform: uppercase; letter-spacing: -0.3px; }
  .hero-button { position: absolute; left: 42px; top: 93px; width: 130px; height: 37px; background: var(--button-red); color: #fff; font-family: "Ubuntu", Arial, sans-serif; font-weight: 500; font-size: 14.5px; line-height: 37px; text-align: center; border-radius: 2px; box-shadow: 0 1px 2px rgba(0,0,0,.4); }
  .hero-next { position: absolute; right: 4px; top: 121px; }
  .hero-dots { position: absolute; left: 357px; top: 279px; width: 39px; height: 11px; border-radius: 6px; background: #fff; display: flex; align-items: center; justify-content: center; gap: 2px; }
  .hero-dots i { width: 6px; height: 6px; border-radius: 50%; background: var(--navy); display: block; }
  .hero-dots i.is-active { background: var(--button-red); }

  /* Services */
  .service { position: absolute; top: 523px; width: 175px; height: 116px; background: var(--card); border: 1px solid var(--card-edge); border-bottom: 6px solid var(--navy); }
  .service::after { content: ""; position: absolute; left: 10px; right: -10px; bottom: -18px; height: 12px; background: radial-gradient(ellipse at top, rgba(0,0,0,.18), rgba(0,0,0,0) 70%); }
  .service-photo { position: absolute; left: 46px; top: -47px; width: 82px; height: 82px; border-radius: 50%; border: 2px solid #fff; box-shadow: 0 1px 3px rgba(0,0,0,.35); }
  .service-title { position: absolute; left: 0; right: 0; top: 43px; text-align: center; font-size: 16px; line-height: 19px; color: var(--brand-red); letter-spacing: -0.3px; }
  .service-more { position: absolute; left: 56px; top: 94px; width: 62px; height: 17px; background: var(--navy); color: #fff; font-size: 8.5px; font-weight: 600; line-height: 17px; text-align: center; }

  /* About */
  .about { position: absolute; left: 101px; top: 707px; width: 540px; }
  .about h2 { font-size: 21px; font-weight: 700; color: var(--navy); letter-spacing: -0.4px; margin-bottom: 9px; }
  .about p { font-size: 16px; font-weight: 300; line-height: 21.6px; color: #333; margin-bottom: 8px; letter-spacing: -0.2px; }

  /* Quote call-out */
  .quote-box { position: absolute; left: 675px; top: 710px; width: 177px; height: 149px; background: var(--navy); border-radius: 2px; }
  .quote-box::after { content: ""; position: absolute; left: 8px; right: 8px; bottom: -20px; height: 14px; background: radial-gradient(ellipse at top, rgba(0,0,0,.2), rgba(0,0,0,0) 70%); }
  .quote-title { position: absolute; left: 0; right: 0; top: 18px; text-align: center; font-family: "Arvo", Georgia, serif; font-weight: 700; font-size: 14.5px; line-height: 22px; color: #fff; text-transform: uppercase; letter-spacing: -0.3px; }
  .quote-button { position: absolute; left: 37px; top: 101px; width: 110px; height: 25px; background: var(--button-red); display: flex; }
  .quote-button span { flex: 1; color: #fff; font-family: "Ubuntu", Arial, sans-serif; font-weight: 700; font-size: 12px; line-height: 25px; padding-left: 8px; }
  .quote-button b { width: 40px; background: var(--button-red-dark); display: flex; align-items: center; justify-content: center; }

  /* Footer */
  .footer-links { position: absolute; left: 0; top: 942px; width: 952px; height: 198px; background: var(--sand); border-bottom: 4px solid var(--sand-line); }
  .footer-col { position: absolute; top: 32px; }
  .footer-col h3 { font-size: 8px; font-weight: 700; color: #222; text-transform: uppercase; margin-bottom: 13px; letter-spacing: 0; }
  .footer-col li { list-style: none; font-size: 7.5px; color: #444; line-height: 17.2px; }
  .footer-col.wide li { line-height: 20px; }
  .footer-col li::before { content: "•"; }
  .site-footer { position: absolute; left: 0; top: 1144px; width: 952px; height: 56px; background: var(--navy-deep); }
  .copyright { position: absolute; left: 99px; top: 22px; font-size: 10px; color: #fff; letter-spacing: -0.2px; }
  .social { position: absolute; left: 767px; top: 20px; display: flex; gap: 7px; }
  .social i { display: block; width: 24px; height: 24px; border-radius: 50%; }
  .social .s1 { background: #1d76b0; }
  .social .s2 { background: #1c9ae0; }
  .social .s3 { background: #3a5a9a; }
</style>
</head>
<body>

<header class="site-header">
  <div class="brand">
    <div class="brand-name">CARGOLINX</div>
    <div class="brand-tagline">A Diversified Freight Company</div>
  </div>
  <div class="contact-phone">
    <svg width="25" height="25" viewBox="0 0 25 25" aria-hidden="true">
      <circle cx="12.5" cy="12.5" r="11.2" fill="none" stroke="#111" stroke-width="2"/>
      <path d="M8.3 6.8c.6-.5 1.4-.4 1.8.2l1.3 2c.3.5.2 1.2-.3 1.6l-.8.6c.6 1.6 1.8 2.9 3.4 3.6l.6-.8c.4-.5 1.1-.6 1.6-.3l2 1.3c.6.4.7 1.2.2 1.8l-.9 1c-.7.7-1.8.9-2.8.5-3.4-1.4-6-4-7.3-7.4-.4-1-.1-2.1.6-2.8z" fill="#111"/>
    </svg>
    <span>(555)204-7190</span>
  </div>
  <nav class="main-nav">
    <a class="is-current" href="#">Home</a>
    <a class="nav-gap" href="#">Insurance &amp; Legal Info</a>
    <a href="#">Fast Freight Quote</a>
  </nav>
</header>

<section class="hero">
  <div class="hero-photo" role="img" aria-label="Photo of a container ship loaded with cargo beside port cranes on blue water"></div>
  <div class="hero-caption">
    <h1 class="hero-title">Get Fast &amp; Free<br>Freight Quotes</h1>
    <div class="hero-button">Learn more</div>
  </div>
  <svg class="hero-next" width="32" height="50" viewBox="0 0 32 50" aria-hidden="true">
    <path d="M4 2 L28 25 L4 48" fill="none" stroke="#3a4150" stroke-width="2.5"/>
  </svg>
  <div class="hero-dots"><i></i><i class="is-active"></i><i></i><i></i></div>
</section>
<div class="hero-shadow"></div>

<article class="service" style="left:100px">
  <div class="service-photo" role="img" aria-label="Container ship at sea" style="background:linear-gradient(160deg,#9fc0de,#5a6f8c 55%,#22364f)"></div>
  <h2 class="service-title">Freight Forwarding<br>Ocean Services</h2>
  <div class="service-more">Read More</div>
</article>
<article class="service" style="left:292px">
  <div class="service-photo" role="img" aria-label="Flatbed truck on a highway" style="background:linear-gradient(160deg,#7c8a6a,#6f7378 50%,#4d5560)"></div>
  <h2 class="service-title">Flatbed, Step Deck &amp;<br>Piggy Back Service</h2>
  <div class="service-more">Read More</div>
</article>
<article class="service" style="left:485px">
  <div class="service-photo" role="img" aria-label="White refrigerated semi truck" style="background:linear-gradient(160deg,#b9c7d4,#e6e8ea 50%,#6d7680)"></div>
  <h2 class="service-title">Dry &amp; Refrigerated<br>Services</h2>
  <div class="service-more">Read More</div>
</article>
<article class="service" style="left:676px">
  <div class="service-photo" role="img" aria-label="Heavy haul truck carrying a large loader" style="background:linear-gradient(160deg,#8aa06c,#b89a3a 50%,#7a2a26)"></div>
  <h2 class="service-title">Heavy Haul<br>Services</h2>
  <div class="service-more">Read More</div>
</article>

<section class="about">
  <h2>About Cargolinx</h2>
  <p>Lorem ipsum is a dummy text only. Dolor sit amet, consectetur adipiscing elit. Nullam felis mauris, eleifend ac rhoncus non, lobortis at diam. Pellentesque suscipit nulla sit amet venenatis porttitor. In augue felis.</p>
  <p>Nulla aliquet, nisi id fermentum rutrum, magna quam vestibulum lacus, id ullamcorper lectus justo sed nisl. In vitae ipsum eget eros fermentum facilisis.</p>
</section>

<aside class="quote-box">
  <div class="quote-title">Get a Free<br>Freight Quote<br>in 2 Minutes</div>
  <div class="quote-button">
    <span>Get Now</span>
    <b><svg width="15" height="15" viewBox="0 0 15 15" aria-hidden="true"><circle cx="7.5" cy="7.5" r="7.5" fill="#fff"/><path d="M3.5 7.5h6M7 4.5l3 3-3 3" fill="none" stroke="#7d1012" stroke-width="2"/></svg></b>
  </div>
</aside>

<section class="footer-links">
  <div class="footer-col wide" style="left:122px">
    <h3>Worldwide Freight Services</h3>
    <ul><li>Worldwide Shipping Scope</li><li>Trucking Shipping Services</li><li>Ocean Shipping Services</li><li>Insurance &amp; Legal Details</li></ul>
  </div>
  <div class="footer-col" style="left:282px">
    <h3>Freight - Trucking Service</h3>
    <ul><li>Heavy Equipment Hauling</li><li>LTL Freight Transport</li><li>Flatbed Transport</li><li>Step Deck Transport</li><li>Dry Van Transport</li><li>Refrigerated Transport</li><li>Power Only &amp; Towaway Transport</li></ul>
  </div>
  <div class="footer-col" style="left:438px">
    <h3>Ocean Shipping Services</h3>
    <ul><li>Heavy Equipment Hauling</li><li>LTL Freight Transport</li><li>Flatbed Transport</li><li>Step Deck Transport</li><li>Dry Van Transport</li><li>Refrigerated Transport</li><li>Power Only &amp; Towaway Transport</li></ul>
  </div>
  <div class="footer-col" style="left:588px">
    <h3>We Ship It All Worldwide</h3>
    <ul><li>Full Loads</li><li>LTL-Less Then Full Loads</li><li>Oversized &amp; Overweight Loads</li><li>500 LBS to 200,000 LBS (No Limits)</li><li>Construction &amp; Mining Equipment</li><li>Mills &amp; Machinery</li><li>Hay &amp; Alfalfa</li></ul>
  </div>
  <div class="footer-col" style="left:741px">
    <h3>Popular Pages</h3>
    <ul><li>Equipment Transport</li><li>Equipment Hauling</li><li>Shipping Service Areas</li></ul>
  </div>
</section>

<footer class="site-footer">
  <p class="copyright">Copyright©2014 Cargolinx. All Rights Reserved.</p>
  <div class="social" aria-label="Social profiles"><i class="s1"></i><i class="s2"></i><i class="s3"></i></div>
</footer>

</body>
</html>
```